Flurwacht.net
Zielgruppe
Hausmeister zum einen bzw. Leute die einen Hausmeister suchen.
Aufgabenstellung
Die Seiten www.flurwacht.net sollen neu gestaltet werden. Hier soll ein Info-Portal entstehen rund um den Hausmeister. Später auch eine Community.
Designt werden soll eine Template-Seite wo wir dann selbst unsere Inhalte einfügen. Wer Lust hat darf auch gerne eine Vorschaltseite entwerfen die diese Domain "würdigt" und dann weiter linkt auf die eigentliche Template Content Seite

```html
<!DOCTYPE html>
<html lang="de">
<head>
<meta charset="utf-8">
<title>Flurwacht.net – Hausmeister Service</title>
<link href="https://fonts.googleapis.com/css2?family=Barlow:ital,wght@0,400;0,500;0,600;0,700;1,300;1,400&display=swap" rel="stylesheet">
<style>
  :root {
    --navy: #1f2f78;
    --navy-dark: #17245e;
    --slate: #5a6496;
    --orange: #f7a21b;
    --orange-dark: #ec8a12;
    --green: #4aa23a;
    --teal: #46b7c4;
    --text: #6b6b6b;
    --page: #f1f1f1;
    --white: #ffffff;
  }
  * { box-sizing: border-box; margin: 0; padding: 0; }
  html, body { width: 1133px; height: 1200px; overflow: hidden; }
  body {
    position: relative;
    background: var(--page);
    font-family: "Barlow", Arial, sans-serif;
    color: var(--text);
  }
  .abs { position: absolute; }

  /* Header */
  .brand {
    left: 59px; top: 55px; height: 47px;
    display: flex; align-items: center; gap: 10px;
    font-weight: 700; font-size: 24px; letter-spacing: 1.5px;
    color: var(--navy);
  }
  .brand-square { width: 14px; height: 14px; background: var(--orange); }
  .lang { top: 38px; right: 62px; font-size: 11px; font-weight: 700; letter-spacing: 1px; }
  .lang span { margin-left: 12px; color: var(--navy); }
  .lang .inactive { color: var(--orange); }
  .main-nav { top: 69px; left: 381px; display: flex; gap: 11px; }
  .main-nav a {
    display: block; height: 25px; line-height: 25px; text-align: center;
    font-size: 13px; font-weight: 600; letter-spacing: 1.3px; color: var(--white);
    text-decoration: none; border-radius: 4px;
    background: linear-gradient(var(--orange), var(--orange-dark));
    box-shadow: 0 2px 3px rgba(0,0,0,.15);
  }
  .main-nav a.active { background: linear-gradient(#6a73a8, #434d8c); }

  .rule { background: var(--navy); height: 4px; left: 58px; width: 1014px; }

  /* Hero */
  .hero { left: 58px; top: 131px; width: 1014px; height: 369px; background: var(--white); }
  .ribbon { right: 0; top: 0; }
  .photo { border-radius: 2px; }
  .crew { left: 44px; top: 25px; width: 304px; height: 341px;
    background: linear-gradient(#e2a046, #a8642a); }
  .tile-circle {
    width: 58px; height: 58px; border-radius: 50%;
    color: var(--white); font-size: 12px; font-weight: 700; letter-spacing: 1px;
    display: flex; align-items: center; justify-content: center;
    box-shadow: 0 2px 4px rgba(0,0,0,.2);
  }
  .tile-img { width: 100px; height: 100px; border-radius: 8px; }
  .tile-label { font-size: 17px; font-weight: 700; letter-spacing: 1px; }
  .all-cats {
    left: 905px; top: 500px; width: 167px; height: 25px; line-height: 25px;
    background: var(--navy); color: var(--white); text-align: center;
    font-size: 13px; font-weight: 700; letter-spacing: 1.3px; border-radius: 0 0 0 6px;
  }

  /* Sidebar */
  .side-title { left: 70px; top: 526px; font-style: italic; font-weight: 300;
    font-size: 31px; line-height: 32px; letter-spacing: 2px; color: var(--slate); }
  .side-sub { left: 70px; top: 608px; font-style: italic; font-size: 17px;
    line-height: 22px; letter-spacing: 1.5px; color: var(--slate); }
  .side-line { left: 70px; top: 705px; width: 216px; height: 2px; background: var(--slate); }
  .news-btn { left: 67px; top: 734px; width: 160px; height: 26px; line-height: 26px;
    text-align: center; color: var(--white); font-size: 13px; font-weight: 700; letter-spacing: 1.3px;
    background: linear-gradient(var(--orange), var(--orange-dark)); border-radius: 4px; }
  .news-box { left: 67px; top: 777px; width: 289px; height: 173px; background: var(--white);
    box-shadow: 0 2px 4px rgba(0,0,0,.06); }
  .worker { left: 102px; top: 985px; width: 234px; height: 128px;
    background: radial-gradient(ellipse at 50% 45%, #8a9bbd, #e9e9e9 70%); }

  /* Content */
  .content { left: 383px; top: 547px; width: 689px; height: 570px; background: var(--white);
    border-top: 3px solid var(--navy); padding: 28px 17px 0 17px; }
  .content h2 { font-size: 13px; font-weight: 700; color: var(--navy); letter-spacing: .6px; margin-bottom: 14px; }
  .content p { font-size: 11px; line-height: 14.5px; margin-bottom: 14px; }
  .content .section { margin-top: 26px; }
  .more-title { font-size: 14px; line-height: 18px; font-weight: 700; color: var(--navy); margin-top: 28px; }
  .duties { list-style: none; margin: 24px 0 0 14px; font-size: 11.5px; line-height: 14px; }
  .duties li::before { content: "* "; }
  .house { left: 429px; top: 384px; width: 247px; height: 157px;
    background: linear-gradient(#8fb8e0 0%, #c9dcea 40%, #d7b98a 60%, #a67f4e 100%); }

  /* Footer */
  .footer { left: 0; top: 1141px; width: 1133px; height: 59px;
    background: linear-gradient(var(--navy-dark), var(--navy)); }
  .foot-nav { left: 67px; top: 20px; display: flex; font-size: 11px; letter-spacing: 1px; color: var(--white); }
  .foot-nav span { padding: 0 12px; border-left: 2px solid var(--white); }
  .foot-nav span:first-child { padding-left: 0; border-left: 0; }
  .copy { right: 61px; top: 21px; font-size: 10px; letter-spacing: .8px; color: var(--white); }
  .copy b { font-weight: 700; }
</style>
</head>
<body>

<div class="abs brand"><span>FLURWACHT.NET</span><span class="brand-square"></span></div>
<div class="abs lang"><span>DEUTSCH</span><span class="inactive">ENGLISH</span></div>
<nav class="abs main-nav">
  <a class="active" href="#" style="width:161px">HAUSMEISTER</a>
  <a href="#" style="width:175px">TIPPS UND TRICKS</a>
  <a href="#" style="width:159px">NEWSLETTER</a>
  <a href="#" style="width:161px">IMPRESSUM</a>
</nav>

<div class="abs rule" style="top:127px"></div>

<section class="abs hero">
  <svg class="abs ribbon" width="50" height="40" viewBox="0 0 50 40"><polygon points="8,0 22,0 50,28 50,40" fill="#f7a21b"/></svg>
  <div class="abs photo crew" role="img" aria-label="Foto: vier Handwerker in Latzhosen mit gelben Helmen und Werkzeug"></div>

  <div class="abs tile-circle" style="left:441px;top:24px;background:var(--teal)">MEHR</div>
  <div class="abs tile-img" role="img" aria-label="Sprühflasche zum Putzen" style="left:520px;top:18px;background:linear-gradient(#dfeef8,#8fc0e6)"></div>
  <div class="abs tile-label" style="left:434px;top:138px;color:var(--navy)">SÄUBERN UND PUTZEN</div>

  <div class="abs tile-circle" style="left:744px;top:24px;background:var(--orange)">MEHR</div>
  <div class="abs tile-img" role="img" aria-label="Werkzeuggürtel mit Bohrmaschine" style="left:800px;top:28px;width:130px;background:linear-gradient(#e4c79a,#8a6a48)"></div>
  <div class="abs tile-label" style="left:731px;top:141px;color:var(--orange)">REPARATUREN</div>

  <div class="abs tile-circle" style="left:441px;top:215px;background:var(--orange-dark)">MEHR</div>
  <div class="abs tile-img" role="img" aria-label="Helm, Hammer und Werkzeuggürtel" style="left:520px;top:200px;width:120px;background:linear-gradient(#7fb9e6,#e5c43a)"></div>
  <div class="abs tile-label" style="left:423px;top:329px;color:var(--orange)">REPARATUREN AM GEBÄUDE</div>

  <div class="abs tile-circle" style="left:744px;top:215px;background:var(--green)">MEHR</div>
  <div class="abs tile-img" role="img" aria-label="Grüne Blätter" style="left:815px;top:220px;width:140px;height:90px;background:radial-gradient(ellipse,#5fb34a,#e9f3e3 72%)"></div>
  <div class="abs tile-label" style="left:731px;top:329px;color:var(--green)">GARTENBAU</div>
</section>

<div class="abs rule" style="top:498px"></div>
<div class="abs all-cats">ALLE KATEGORIEN</div>

<aside>
  <h1 class="abs side-title">HAUSMEISTER<br>SERVICE</h1>
  <p class="abs side-sub">HAUSMEISTER DIENSTE SOWIE<br>HAUSMEISTER FIRMEN<br>VERZEICHNIS INFORMATIONEN<br>RUND UM DEN HAUSMEISTER</p>
  <div class="abs side-line"></div>
  <div class="abs news-btn">NACHRICHTEN</div>
  <div class="abs news-box"></div>
  <div class="abs photo worker" role="img" aria-label="Foto: Handwerker kniet und misst mit Zollstock"></div>
</aside>

<main class="abs content">
  <h2>BEGRIFFSERKLÄRUNG DER HAUSMEISTER</h2>
  <p>Zuerst einmal wollen wir den Begriff Hausmeister erklären. Hier hilft ein Blick in die freie Enzyklopädie Wissenswiki!</p>
  <p>Der Hausmeister - in anderen Ländern und umgangssprachlich auch Hauswart, Portier, Concierge oder Hausbesorger genannt - sorgt für die Ordnung und Sauberkeit und kümmert sich um die Haustechnik. In Gebäuden oder Wohnanlagen sind es meist kleinere Reparaturarbeiten wie Auswechseln von Glühbirnen oder Anschrauben von Gegenständen bis hin zur Wartung der Haustechnik oder auch Reinigung des Gebäudes. Natürlich fallen auch arbeiten rund um das Gebäude an wie Rasen mähen, Müllbeseitigung und vieles mehr. Natürlich schaut der Hausmeister auch "nach dem Rechten" und hält die Zugänge zum Haus frei - zum Beispiel im Winter durch Schnee schaufeln oder streuen von Salz oder ähnlichem.</p>
  <h2 class="section">TÄTIGKEITSFELDER DES HAUSMEISTERS</h2>
  <p>Grob gesagt gehört es zu den Aufgaben eines Hausmeisters, sich um alle Belange zu kümmern, die rund um ein Haus anfallen. Auch wenn bestimmte Arbeiten auch gerne externen Dienstleistern übertragen werden (etwa dann wenn ein einzelner Hausmeister mit der Arbeit überfordert ist wie eine komplette Gebäudereinigung oder der Winterdienst) so ist es doch letzten Endes der Hausmeister selbst, der sich Angebote von externen Dienstleistern einholt, diese an den Hauseigentümer oder die Hausverwaltung weiter leitet und zu guter letzt sich vergewissert ob alle vergebenen Arbeiten korrekt ausgeführt werden.</p>
  <p class="more-title">Zu den Tätigkeiten eines<br>Hausmeisters gehört weiterhin:</p>
  <ul class="duties">
    <li>Kontrolle von Arbeiten und Handwerken bei Auftragsarbeiten</li>
    <li>Durchführung von Sommer- und Winterdienstarbeiten</li>
    <li>Kontrolle und Überwachung von Lüftungs- und Heizungsanlagen</li>
    <li>Durchführung von Kleinreparaturen und Wartungsarbeiten</li>
    <li>Reinigung von Gebäuden und Objekten</li>
    <li>Reinhaltung von Wegen und Grünflächen</li>
    <li>Pflege von Grünflächen und Wegen (Fegen und Müharbeiten)</li>
  </ul>
  <div class="abs photo house" role="img" aria-label="Foto: Bauarbeiter mit Bauplan vor einem Wohnhaus im Bau"></div>
</main>

<footer class="abs footer">
  <div class="abs foot-nav"><span>HAUSMEISTER</span><span>TIPPS UND TRICKS</span><span>NEWSLETTER</span><span>IMPRESSUM</span></div>
  <div class="abs copy">©2010 <b>FLURWACHT.NET</b> ALL RIGHTS RESERVED.</div>
</footer>

</body>
</html>
```